Ardo Move - A non profit for healthy lifestyle and fitness within refugee camps

We need a logo and website design for a new 501c3 Non-Profit based in San Francisco called 'Ardo Move'. We help coordinate trips across the globe to provide fitness classes to refugee camps to help refugees maintain a healthy lifestyle and fun while exercising.
Our first trip was to Greece and we hope to extend our reach by working with other non-profits to coordinate how we can help bring a healthy lifestyle and a wellness to refugees in need.
We would like to see website design that use the color green and blue. The final design should represent a welcoming website to encourage people to take a trip either by themselves, as a group, or with a corporate team.
We have 3 certified and experienced trainers that will be running these trips and with a hope of 20 volunteers per trip to help.

We are hoping to partner with another 501c3 called 'Tide of Hope' which I have participated in and with the hopes of providing an easier and simpler user experience than their current website but with many of the same content.

We would like a 'Trips' page with previous trips, 'Trainers/Hosts' page with bios of the leaders hosting the event, 'Register Page' for folks to register for upcoming trips, 'About Us' page for our mission statement and work, 'Albums' page for photos taken on the trip, 'Contact Us' page for FAQs and questions to submit, and a 'Donate' page for people to donate to our cause.

I would like this page to be created in Word Press.

ie: http://www.tideofhopeexample.com.au/programs/

Target Market(s)

Volunteers, non-profit partners

Industry/Entity Type

Non-Profit

Number of Pages Required

4 page

Font styles to use
Sans Serif

Colors

Designer to choose colors to be used in the design.

Requirements
Must have
• 'Trips' page with previous trips, 'Trainers/Hosts' page with bios of the leaders hosting the event, 'Register Page' for folks to register for upcoming trips, 'About Us' page for our mission statement and work, 'Albums' page for photos taken on the trip, 'Contact Us' page for FAQs and questions to submit, and a 'Donate' page for people to donate to our cause.

```html
<!DOCTYPE html>
<html lang="en">
<head>
<meta charset="utf-8">
<title>Ardo Move – Fitness for Refugee Camps</title>
<link rel="stylesheet" href="https://fonts.googleapis.com/css2?family=Oswald:wght@500;700&family=Montserrat:wght@500;600;700&family=Open+Sans:wght@400;600&display=swap">
<style>
:root{
  --gold:#b8935a;
  --gold-dark:#a27d45;
  --ink:#222222;
  --text:#555555;
  --muted:#8a8a8a;
  --light:#f1f1f1;
  --white:#ffffff;
  --night:#1c2026;
  --footer:#e9e9e9;
}
*{margin:0;padding:0;box-sizing:border-box}
html,body{width:1200px;height:3540px;overflow:hidden}
body{font-family:'Open Sans',Arial,sans-serif;color:var(--text);background:var(--white);font-size:15px;line-height:1.6}
.page{position:relative;width:1200px;height:3540px}

/* header */
.site-header{position:absolute;top:0;left:0;width:1200px;height:88px;z-index:3;display:flex;align-items:center;justify-content:space-between;padding:0 40px 0 72px;background:rgba(255,255,255,.92)}
.brand{font-family:'Montserrat',Arial,sans-serif;font-weight:700;font-size:28px;letter-spacing:1px;color:var(--ink);display:flex;align-items:center;gap:12px;white-space:nowrap}
.brand-dot{width:14px;height:14px;background:var(--gold);border-radius:50%}
.main-nav{display:flex;height:88px}
.main-nav a{display:flex;align-items:center;padding:0 14px;font-family:'Montserrat',Arial,sans-serif;font-size:14px;font-weight:600;color:var(--ink);text-decoration:none;white-space:nowrap}
.main-nav a.is-active{background:var(--gold);color:var(--white);padding:0 20px}

/* hero */
.hero{position:absolute;top:0;left:0;width:1200px;height:600px;background:linear-gradient(180deg,#5d6166 0%,#7a7460 45%,#4a4036 100%);color:var(--white);text-align:center}
.hero-photo{position:absolute;inset:0;background:radial-gradient(ellipse at 50% 80%,rgba(160,120,80,.45),transparent 60%),linear-gradient(90deg,rgba(40,40,40,.45),rgba(40,40,40,.15),rgba(40,40,40,.45))}
.hero-title{position:absolute;top:196px;left:0;width:100%;font-family:'Oswald',Arial,sans-serif;font-weight:700;font-size:58px;letter-spacing:2px}
.hero-lead{position:absolute;top:290px;left:220px;width:760px;font-size:17px;line-height:1.7}
.hero .btn{position:absolute;top:396px;left:540px}
.slider-arrow{position:absolute;top:320px;width:40px;height:60px}
.slider-arrow.prev{left:30px}
.slider-arrow.next{right:30px}

.btn{display:inline-block;width:120px;height:42px;line-height:42px;text-align:center;background:var(--gold);color:var(--white);font-family:'Montserrat',Arial,sans-serif;font-size:13px;font-weight:600;text-decoration:none}
.btn-small{width:110px;height:36px;line-height:36px;font-size:12px}
.btn-dark{background:var(--ink)}

/* about */
.about{position:absolute;top:600px;left:0;width:1200px;height:560px;background:var(--white)}
.about-photo{position:absolute;top:80px;left:100px;width:400px;height:392px;border:6px solid var(--white);box-shadow:0 0 0 2px var(--gold);background:linear-gradient(135deg,#7a9bb8,#c9b08a 50%,#8a6a4c)}
.about-body{position:absolute;top:110px;left:564px;width:540px}
.about-kicker{font-family:'Oswald',Arial,sans-serif;font-weight:700;font-size:44px;color:var(--ink);line-height:1.1}
.about-title{font-family:'Oswald',Arial,sans-serif;font-weight:700;font-size:66px;color:var(--gold);line-height:1.1;letter-spacing:1px}
.about-text{margin-top:20px;font-size:14px;color:var(--muted);line-height:1.75}
.about-body .btn{margin-top:34px}

/* section titles */
.section-title{font-family:'Montserrat',Arial,sans-serif;font-weight:600;font-size:24px;color:var(--gold);text-align:center;letter-spacing:1px;text-transform:uppercase}
.section-title::after{content:"";display:block;width:60px;height:2px;background:var(--gold);margin:14px auto 0}

/* training */
.training{position:absolute;top:1160px;left:0;width:1200px;height:680px;background:var(--light);padding-top:64px}
.cards{position:absolute;top:172px;left:152px;display:flex;gap:44px}
.card{width:300px;text-align:center}
.card-photo{height:220px;border:4px solid var(--white)}
.card-photo.p1{background:linear-gradient(135deg,#6f7f94,#c7a07c,#4a3b33)}
.card-photo.p2{background:linear-gradient(180deg,#aab7c6,#b49a7e 60%,#7d6650)}
.card-photo.p3{background:linear-gradient(135deg,#b55a4a,#d8b28a,#5b4a3e)}
.card-title{margin-top:28px;font-family:'Montserrat',Arial,sans-serif;font-weight:600;font-size:17px;color:var(--ink);text-transform:uppercase}
.card-text{margin:10px 18px 0;font-size:13px;color:var(--muted);line-height:1.6}
.card .btn{margin-top:18px;position:relative;z-index:1}
.card-rule{height:1px;background:#cfcfcf;margin:-18px 0 0;position:relative;z-index:0}

/* videos */
.videos{position:absolute;top:1840px;left:0;width:1200px;height:640px;background:linear-gradient(180deg,#2b3038,#161a20);padding-top:76px}
.videos .section-title{color:var(--white)}
.videos .section-title::after{display:none}
.video-frame{position:absolute;top:192px;left:248px;width:704px;height:360px;border:4px solid rgba(255,255,255,.85);background:linear-gradient(135deg,#6c7d57,#b98c6a 45%,#b64b3d 75%,#5d6b3f)}
.play{position:absolute;top:150px;left:322px}
.video-arrow{position:absolute;top:350px;width:60px;height:60px}
.video-arrow.prev{left:102px}
.video-arrow.next{right:102px}

/* services */
.services{position:absolute;top:2480px;left:0;width:1200px;height:560px;background:var(--white);padding-top:76px}
.service-grid{position:absolute;top:200px;left:100px;display:grid;grid-template-columns:repeat(3,300px);column-gap:52px;row-gap:44px}
.service{display:flex;gap:18px}
.service svg{flex:none;width:48px;height:48px}
.service-name{font-family:'Montserrat',Arial,sans-serif;font-weight:600;font-size:15px;color:var(--ink)}
.service-text{font-size:12.5px;color:var(--muted);line-height:1.6;margin-top:4px}

/* subscribe + contact */
.subscribe{position:absolute;top:3040px;left:100px;width:460px;height:416px;background:var(--gold);color:var(--white);padding:36px 40px;text-align:center}
.subscribe h3{font-family:'Montserrat',Arial,sans-serif;font-weight:600;font-size:20px;letter-spacing:1px}
.subscribe p{font-size:13px;margin:10px 30px 22px;line-height:1.6}
.field{display:block;height:42px;border-bottom:1px solid rgba(255,255,255,.7);text-align:left;font-size:13px;line-height:42px;color:rgba(255,255,255,.9);margin-bottom:6px}
.subscribe-foot{display:flex;align-items:center;gap:24px;margin-top:22px}
.btn-outline{border:1px solid var(--white);background:transparent}
.subscribe-foot span{font-size:12px}

.contact{position:absolute;top:3070px;left:608px;width:492px}
.contact-name{font-family:'Montserrat',Arial,sans-serif;font-weight:600;font-size:26px;color:var(--ink)}
.contact-name::after{content:"";display:block;width:60px;height:2px;background:var(--gold);margin-top:14px}
.contact h4{margin-top:30px;font-family:'Montserrat',Arial,sans-serif;font-weight:600;font-size:18px;color:var(--ink)}
.contact p{margin-top:12px;font-size:13px;color:var(--muted);line-height:1.7}
.contact-line{display:flex;align-items:center;gap:14px;margin-top:26px;font-size:15px;color:var(--text)}
.contact-line svg{width:40px;height:40px;flex:none}

/* footer */
.site-footer{position:absolute;top:3480px;left:0;width:1200px;height:60px;background:var(--footer);display:flex;align-items:center;justify-content:space-between;padding:0 100px;font-size:13px;color:var(--text)}
.social{display:flex;gap:10px}
.social span{width:30px;height:30px;border:1.5px solid #777;border-radius:50%}
</style>
</head>
<body>
<div class="page">

  <section class="hero">
    <div class="hero-photo" role="img" aria-label="Photo of children and volunteers exercising together outside tents in a refugee camp"></div>
    <h1 class="hero-title">WELCOME ARDO MOVE</h1>
    <p class="hero-lead">We help coordinate trips across the globe to provide fitness classes to refugee camps to help refugees maintain a healthy lifestyle and fun while exercising.</p>
    <a class="btn" href="#">Read More</a>
    <svg class="slider-arrow prev" viewBox="0 0 40 60"><polyline points="28,8 10,30 28,52" fill="none" stroke="#fff" stroke-width="3"/></svg>
    <svg class="slider-arrow next" viewBox="0 0 40 60"><polyline points="12,8 30,30 12,52" fill="none" stroke="#fff" stroke-width="3"/></svg>
  </section>

  <header class="site-header">
    <div class="brand"><span class="brand-dot"></span>ARDO MOVE</div>
    <nav class="main-nav">
      <a class="is-active" href="#">Home</a>
      <a href="#">About Us</a>
      <a href="#">Trips</a>
      <a href="#">Trainer/ Hosts</a>
      <a href="#">Register</a>
      <a href="#">Albums</a>
      <a href="#">Donate</a>
      <a href="#">FAQ</a>
      <a href="#">Contact Us</a>
    </nav>
  </header>

  <section class="about">
    <div class="about-photo" role="img" aria-label="Photo of a group joining hands in a circle"></div>
    <div class="about-body">
      <div class="about-kicker">ARDO MOVE</div>
      <h2 class="about-title">TRAINING CLASSES</h2>
      <p class="about-text">We bring certified trainers and caring volunteers into refugee camps, running open fitness classes that anyone can join. Every session builds strength, lifts spirits and gives families a shared hour of movement, music and play. Trips leave several times each year, and you are welcome to join us.</p>
      <a class="btn" href="#">Read More</a>
    </div>
  </section>

  <section class="training">
    <h2 class="section-title">Our Fitness Training</h2>
    <div class="cards">
      <article class="card">
        <div class="card-photo p1" role="img" aria-label="Photo of a family in a refugee camp"></div>
        <h3 class="card-title">Nemo Enim Ipsam</h3>
        <p class="card-text">Our signature 60 minute all level class uses slow and controlled movements that build strength in a gentle, steady way.</p>
        <a class="btn btn-small btn-dark" href="#">READ MORE</a>
        <div class="card-rule"></div>
      </article>
      <article class="card">
        <div class="card-photo p2" role="img" aria-label="Photo of children standing in a camp yard"></div>
        <h3 class="card-title">Voluptatem Quia</h3>
        <p class="card-text">Our signature 60 minute all level class uses slow and controlled movements that build strength in a gentle, steady way.</p>
        <a class="btn btn-small" href="#">READ MORE</a>
        <div class="card-rule"></div>
      </article>
      <article class="card">
        <div class="card-photo p3" role="img" aria-label="Photo of smiling children outdoors"></div>
        <h3 class="card-title">Perspiciatis Unde Omnis</h3>
        <p class="card-text">Our signature 60 minute all level class uses slow and controlled movements that build strength in a gentle, steady way.</p>
        <a class="btn btn-small btn-dark" href="#">READ MORE</a>
        <div class="card-rule"></div>
      </article>
    </div>
  </section>

  <section class="videos">
    <h2 class="section-title">Fitness Camp Videos</h2>
    <div class="video-frame" role="img" aria-label="Video still of two children stretching with hands behind their heads">
      <svg class="play" width="60" height="60" viewBox="0 0 60 60"><circle cx="30" cy="30" r="28" fill="rgba(0,0,0,.55)" stroke="#fff" stroke-width="2"/><polygon points="24,18 44,30 24,42" fill="#fff"/></svg>
    </div>
    <svg class="video-arrow prev" viewBox="0 0 60 60"><circle cx="30" cy="30" r="28" fill="none" stroke="#fff" stroke-width="2"/><polyline points="34,20 24,30 34,40" fill="none" stroke="#fff" stroke-width="3"/></svg>
    <svg class="video-arrow next" viewBox="0 0 60 60"><circle cx="30" cy="30" r="28" fill="none" stroke="#fff" stroke-width="2"/><polyline points="26,20 36,30 26,40" fill="none" stroke="#fff" stroke-width="3"/></svg>
  </section>

  <section class="services">
    <h2 class="section-title">Our Fitness Services</h2>
    <div class="service-grid">
      <div class="service">
        <svg viewBox="0 0 48 48"><path d="M8 34 L18 20 L26 26 L40 14" fill="none" stroke="#222" stroke-width="5" stroke-linecap="round"/><circle cx="10" cy="14" r="5" fill="#222"/></svg>
        <div><div class="service-name">Fitness</div><p class="service-text">Nemo enim ipsam voluptatem quia voluptas sit aspernatur aut odit aut fugit dolores.</p></div>
      </div>
      <div class="service">
        <svg viewBox="0 0 48 48"><polygon points="24,6 44,40 4,40" fill="var(--gold)"/><polygon points="24,22 32,40 16,40" fill="#fff"/></svg>
        <div><div class="service-name">Refugee Camps</div><p class="service-text">Nemo enim ipsam voluptatem quia voluptas sit aspernatur aut odit aut fugit dolores.</p></div>
      </div>
      <div class="service">
        <svg viewBox="0 0 48 48"><rect x="4" y="16" width="8" height="16" fill="#222"/><rect x="36" y="16" width="8" height="16" fill="#222"/><rect x="12" y="21" width="24" height="6" fill="#222"/></svg>
        <div><div class="service-name">Exercising</div><p class="service-text">Nemo enim ipsam voluptatem quia voluptas sit aspernatur aut odit aut fugit dolores.</p></div>
      </div>
      <div class="service">
        <svg viewBox="0 0 48 48"><circle cx="14" cy="12" r="5" fill="#222"/><circle cx="34" cy="12" r="5" fill="#222"/><path d="M6 40 L14 20 L22 40 M26 40 L34 20 L42 40" fill="none" stroke="#222" stroke-width="5" stroke-linejoin="round"/></svg>
        <div><div class="service-name">Fitness Classes</div><p class="service-text">Nemo enim ipsam voluptatem quia voluptas sit aspernatur aut odit aut fugit dolores.</p></div>
      </div>
      <div class="service">
        <svg viewBox="0 0 48 48"><path d="M24 42 C8 30 4 22 4 15 C4 9 9 5 14 5 C18 5 22 8 24 12 C26 8 30 5 34 5 C39 5 44 9 44 15 C44 22 40 30 24 42Z" fill="var(--gold)"/></svg>
        <div><div class="service-name">Healthy Lifestyle</div><p class="service-text">Nemo enim ipsam voluptatem quia voluptas sit aspernatur aut odit aut fugit dolores.</p></div>
      </div>
      <div class="service">
        <svg viewBox="0 0 48 48"><circle cx="24" cy="24" r="18" fill="none" stroke="#222" stroke-width="5"/><polyline points="15,24 22,31 34,17" fill="none" stroke="#222" stroke-width="5"/></svg>
        <div><div class="service-name">Ardo Move</div><p class="service-text">Nemo enim ipsam voluptatem quia voluptas sit aspernatur aut odit aut fugit dolores.</p></div>
      </div>
    </div>
  </section>

  <section class="subscribe">
    <h3>SUBSCRIBE</h3>
    <p>Sign up with your email address to receive the latest news and updates.</p>
    <span class="field">First Name</span>
    <span class="field">Last Name</span>
    <span class="field">Email Address</span>
    <div class="subscribe-foot">
      <a class="btn btn-small btn-outline" href="#">SIGN UP</a>
      <span>We respect your privacy</span>
    </div>
  </section>

  <section class="contact">
    <div class="contact-name">ARDO MOVE</div>
    <h4>Got a question or comment?</h4>
    <p>We are constantly working to raise the bar on our services. If you have any questions or concerns about your experience, please let us know.</p>
    <div class="contact-line">
      <svg viewBox="0 0 40 40"><circle cx="20" cy="20" r="19" fill="none" stroke="#bbb"/><rect x="11" y="14" width="18" height="12" fill="none" stroke="#555" stroke-width="1.6"/><polyline points="11,14 20,21 29,14" fill="none" stroke="#555" stroke-width="1.6"/></svg>
      Mail Us At: info@ardomove.org
    </div>
    <div class="contact-line">
      <svg viewBox="0 0 40 40"><circle cx="20" cy="20" r="19" fill="none" stroke="#bbb"/><path d="M14 12 L18 12 L19 17 L17 18 C18 21 19 22 22 23 L23 21 L28 22 L28 26 C20 27 13 20 14 12Z" fill="#555"/></svg>
      Call Us At: +1 800 555 0142
    </div>
  </section>

  <footer class="site-footer">
    <span>Copyright © 2017 Ardo Move. All Right Reserved</span>
    <div class="social"><span></span><span></span><span></span><span></span><span></span></div>
  </footer>

</div>
</body>
</html>
```